File your income taxes and walk away with cash today. direct mailer campaign

We prepare income tax returns. Our slogan is Walk away with cash today! Our marketing edge above our competition is the fact that clients can get up to $5000 the day they file. We also offer notary, payroll, and bookkeeping services. We would like something with cash on the card as well. Plume Quick Returns is the name of our company and this campaign is actually for a direct mailer to client prospects that make under 25k a year, who will be looking for help preparing their income tax documents but also be looking for cash the same day they file. Our office will begin handing out checks on January 2nd!

Target Market(s)

My target market for this particular piece is Blacks and Hispanics of lower income.

Industry/Entity Type

Finance And Accounting

Font styles to use
Serif
Script

Colors
a54499
b768aa
33a6d7
33b8a4
e667a6
e34197

Requirements
Must have
• Plume Quick Returns should be written is some form of script, prefer colors of Purple & aqua or Pink and Turquoise. Some form of cash that looks as real as possible.
Nice to have
• Here is our contact info:
• 482 North K M Hallworth Parkway
• Dallas, TX 75418
• (281) 604-3397
• www.plumequickreturns.example
Should not have
• No white people or body parts

```html
<!DOCTYPE html>
<html lang="en">
<head>
<meta charset="utf-8">
<title>Plume Quick Returns – Direct Mailer</title>
<link rel="stylesheet" href="https://fonts.googleapis.com/css2?family=Oswald:wght@500;700&family=Pathway+Gothic+One&display=swap">
<style>
  :root {
    --teal-dark: #0d6f7e;
    --teal: #2a9a98;
    --teal-light: #5cbfae;
    --magenta: #e0268f;
    --purple: #a54499;
    --gold: #c99a3a;
    --gold-light: #e8c874;
    --navy: #1c4a9c;
    --white: #ffffff;
    --stage: #a9a9a9;
  }
  * { margin: 0; padding: 0; box-sizing: border-box; }
  html, body { width: 961px; height: 1200px; overflow: hidden; }
  body {
    background: radial-gradient(ellipse at 50% 50%, #d6d6d6 0%, var(--stage) 55%, #8e8e8e 100%);
    position: relative;
    font-family: "Pathway Gothic One", "Oswald", sans-serif;
  }
  .card {
    position: absolute;
    left: 138px;
    width: 687px;
    height: 535px;
    overflow: hidden;
    box-shadow: 0 4px 14px rgba(0,0,0,0.25);
  }
  .card--front { top: 42px; background: linear-gradient(135deg, var(--teal-dark), var(--teal) 55%, var(--teal-light)); }
  .card--back { top: 610px; background: var(--white); }
  .card svg.shapes { position: absolute; inset: 0; }
  .photo-area {
    position: absolute; inset: 0;
  }
  .offer {
    position: absolute; right: 32px; top: 0; text-align: right; color: var(--white);
  }
  .offer span { position: absolute; right: 0; white-space: nowrap; }
  .headline {
    font-family: "Oswald", sans-serif; font-weight: 700; color: var(--gold-light);
    background: linear-gradient(180deg, #f1d98b, #c2912f);
    -webkit-background-clip: text; background-clip: text; color: transparent;
  }
  .headline--big { font-size: 38px; line-height: 1; }
  .headline--small { font-size: 23px; line-height: 1; font-weight: 500; }
  .offer .amount { font-family: "Oswald", sans-serif; font-weight: 700; font-size: 27px; line-height: 1; }
  .offer .point { font-size: 21px; line-height: 1; }
  .brand-name {
    position: absolute; text-align: center; white-space: nowrap;
    font-family: "Oswald", sans-serif; font-weight: 500; color: var(--gold);
    font-size: 40px; line-height: 1;
  }
  .brand-url {
    position: absolute; text-align: center; white-space: nowrap;
    font-size: 20px; color: var(--navy); line-height: 1;
  }
  .contact { position: absolute; left: 33px; top: 0; color: var(--navy); }
  .contact .manager {
    position: absolute; top: 150px; white-space: nowrap;
    font-family: "Oswald", sans-serif; font-weight: 700; font-size: 27px; line-height: 1;
  }
  .contact .row { position: absolute; left: 0; white-space: nowrap; display: flex; align-items: center; gap: 6px; line-height: 1; }
  .contact .row svg { width: 20px; height: 20px; flex: none; }
  .contact .row--text { font-size: 20px; }
  .contact .row--number { font-family: "Oswald", sans-serif; font-weight: 700; font-size: 22px; }
  .contact .line { position: absolute; left: 26px; white-space: nowrap; font-size: 20px; line-height: 1; }
  .back-slogan { position: absolute; left: 37px; }
  .back-slogan span { position: absolute; left: 0; white-space: nowrap; }
  .cash-art {
    position: absolute; left: 232px; top: 218px; width: 250px; height: 284px;
    border-radius: 120px 120px 18px 18px;
    background: linear-gradient(160deg, #e7c25a 0%, #d9d9d2 35%, #b9c9a2 65%, #8aa36b 100%);
  }
  .sticker {
    position: absolute; left: 384px; top: 124px; width: 160px; height: 160px; border-radius: 50%;
    background: radial-gradient(circle at 35% 35%, var(--magenta), var(--purple));
    display: flex; align-items: center; justify-content: flex-start;
  }
  .sticker::before {
    content: ""; position: absolute; inset: 6px; border-radius: 50%;
    border: 1.5px dashed rgba(255,255,255,0.8);
  }
  .sticker p {
    position: relative; margin-left: 29px;
    font-family: "Oswald", sans-serif; font-weight: 500; color: var(--white);
    font-size: 16px; line-height: 23px; text-transform: uppercase;
  }
  .stamp-box { position: absolute; left: 583px; top: 23px; width: 77px; height: 213px; background: var(--white); border: 1px solid #333; }
  .address-box { position: absolute; left: 480px; top: 299px; width: 208px; height: 237px; background: var(--white); border: 1px solid #333; }
</style>
</head>
<body>

<section class="card card--front" aria-label="Mailer front">
  <svg class="shapes" viewBox="0 0 687 535" width="687" height="535" aria-hidden="true">
    <defs>
      <linearGradient id="goldBand" x1="0" y1="0" x2="1" y2="0">
        <stop offset="0" stop-color="#a8772a"/><stop offset="0.5" stop-color="#f2d57e"/><stop offset="1" stop-color="#b9862f"/>
      </linearGradient>
      <linearGradient id="photoTone" x1="0" y1="0" x2="1" y2="1">
        <stop offset="0" stop-color="#2b3540"/><stop offset="0.55" stop-color="#4f6f9c"/><stop offset="1" stop-color="#bfc6b4"/>
      </linearGradient>
    </defs>
    <!-- magenta crescent framing the photo -->
    <path d="M0,0 H390 C470,120 430,300 300,360 C200,405 80,405 0,395 Z" fill="var(--magenta)"/>
    <path d="M0,0 H370 C440,120 400,290 280,345 C190,385 80,385 0,378 Z" fill="var(--purple)" opacity="0.55"/>
    <!-- gold sweep -->
    <path d="M0,430 C180,360 360,300 470,0 H482 C380,320 200,395 0,452 Z" fill="url(#goldBand)"/>
    <g fill="none" stroke="#e9cf7d" stroke-width="1.2">
      <path d="M0,470 C190,400 380,330 492,0"/>
      <path d="M0,480 C195,410 388,338 500,0"/>
      <path d="M0,490 C200,420 396,346 508,0"/>
      <path d="M0,500 C205,430 404,354 516,0"/>
      <path d="M0,510 C210,440 412,362 524,0"/>
    </g>
    <!-- white base -->
    <path d="M0,535 V520 C180,450 400,420 560,420 C620,420 660,418 687,412 V535 Z" fill="var(--white)"/>
    <!-- lower-right swoosh -->
    <path d="M520,535 C600,500 660,460 687,390 V535 Z" fill="var(--magenta)"/>
    <path d="M600,535 C640,510 672,480 687,450 V472 C672,500 650,520 625,535 Z" fill="url(#goldBand)"/>
  </svg>

  <div class="photo-area">
    <svg viewBox="0 0 687 535" width="687" height="535" role="img" aria-label="Photo: smiling woman in a blue sweater holding out a fan of hundred-dollar bills">
      <path d="M0,0 H362 C425,120 385,285 270,335 C185,372 80,372 0,365 Z" fill="url(#photoTone)"/>
    </svg>
  </div>

  <div class="offer">
    <span class="headline headline--big" style="top:58px">WALK AWAY</span>
    <span class="headline headline--small" style="top:106px">WITH CASH TODAY!</span>
    <span class="amount" style="top:148px">UP TO $5000</span>
    <span class="point" style="top:183px">same day you file!</span>
    <span class="point" style="top:211px">15 years of tax experience!</span>
    <span class="point" style="top:239px">We will get your maximum refund!</span>
    <span class="point" style="top:268px">Submit documents securely from home!</span>
    <span class="amount" style="top:309px">HASTA $5000 HOY!</span>
    <span class="point" style="top:342px">15 anos de experiencia en impuestos!</span>
    <span class="point" style="top:370px">Obtendremos su reembolso maximo!</span>
  </div>

  <div class="brand-name" style="left:188px; width:360px; top:444px">Plume Quick Returns</div>
  <div class="brand-url" style="left:188px; width:360px; top:494px">www.plumequickreturns.example</div>
</section>

<section class="card card--back" aria-label="Mailer back">
  <svg class="shapes" viewBox="0 0 687 535" width="687" height="535" aria-hidden="true">
    <defs>
      <linearGradient id="tealBack" x1="0" y1="0" x2="0" y2="1">
        <stop offset="0" stop-color="var(--teal-light)"/><stop offset="1" stop-color="var(--teal-dark)"/>
      </linearGradient>
      <linearGradient id="goldBack" x1="0" y1="1" x2="1" y2="0">
        <stop offset="0" stop-color="#a8772a"/><stop offset="0.5" stop-color="#f2d57e"/><stop offset="1" stop-color="#b9862f"/>
      </linearGradient>
    </defs>
    <!-- magenta band -->
    <path d="M90,535 C300,470 450,330 430,170 C422,100 420,40 414,0 H440 C450,60 456,120 460,180 C470,340 340,480 170,535 Z" fill="var(--magenta)"/>
    <!-- gold band -->
    <path d="M160,535 C330,480 455,340 450,180 C447,110 440,50 432,0 H462 C472,60 478,120 480,180 C485,350 370,480 220,535 Z" fill="url(#goldBack)"/>
    <g fill="none" stroke="#e9cf7d" stroke-width="1.2">
      <path d="M235,535 C390,480 492,350 488,180 C486,110 480,50 472,0"/>
      <path d="M245,535 C400,480 500,350 496,180 C494,110 488,50 480,0"/>
      <path d="M255,535 C410,480 508,350 504,180 C502,110 496,50 488,0"/>
    </g>
    <!-- teal field -->
    <path d="M265,535 C420,480 516,350 512,180 C510,110 504,50 496,0 H687 V535 Z" fill="url(#tealBack)"/>
  </svg>

  <div class="brand-name" style="left:30px; width:380px; top:38px">Plume Quick Returns</div>
  <div class="brand-url" style="left:30px; width:380px; top:90px">www.plumequickreturns.example</div>

  <div class="contact">
    <div class="manager">RENATA SOLIS, MANAGER</div>
    <div class="row row--text" style="top:196px">
      <svg viewBox="0 0 20 20" aria-hidden="true"><rect x="1.5" y="4" width="17" height="12" fill="none" stroke="var(--gold)" stroke-width="1.6"/><path d="M1.5,4 L10,11 L18.5,4" fill="none" stroke="var(--gold)" stroke-width="1.6"/></svg>
      <span>renatasolis@plumequickreturns.example</span>
    </div>
    <div class="row row--number" style="top:224px">
      <svg viewBox="0 0 20 20" aria-hidden="true"><path d="M5,2 L8,6 L6.5,8 C7.5,10.5 9.5,12.5 12,13.5 L14,12 L18,15 L16.5,18 C9,18 2,11 2,3.5 Z" fill="var(--gold)"/></svg>
      <span>(281) 604-3397</span>
    </div>
    <div class="row row--number" style="top:256px">
      <svg viewBox="0 0 20 20" aria-hidden="true"><rect x="5" y="2" width="10" height="5" fill="var(--gold)"/><rect x="1" y="7" width="18" height="8" rx="1.5" fill="var(--gold)"/><rect x="5" y="12" width="10" height="6" fill="#fff" stroke="var(--gold)" stroke-width="1.5"/></svg>
      <span>(208) 555-0142</span>
    </div>
    <div class="row row--text" style="top:289px">
      <svg viewBox="0 0 20 20" aria-hidden="true"><path d="M10,1 C6,1 3.5,4 3.5,7.5 C3.5,12 10,19 10,19 C10,19 16.5,12 16.5,7.5 C16.5,4 14,1 10,1 Z" fill="var(--gold)"/><circle cx="10" cy="7.5" r="2.6" fill="#fff"/></svg>
      <span>482 North K M</span>
    </div>
    <div class="line" style="top:318px">Hallworth Parkway</div>
    <div class="line" style="top:347px">Dallas, TX 75418</div>
  </div>

  <div class="back-slogan">
    <span class="headline headline--big" style="top:382px">WALK AWAY</span>
    <span class="headline headline--small" style="top:424px">WITH CASH TODAY!</span>
  </div>

  <div class="cash-art" role="img" aria-label="Illustration: gold wall clock above stacks of banded dollar bills and gold coins"></div>

  <div class="sticker"><p>Our office will<br>be handing out<br>checks on<br>January 2</p></div>

  <div class="stamp-box" aria-label="Postage area"></div>
  <div class="address-box" aria-label="Mailing address area"></div>
</section>

</body>
</html>
```